New Business Card Design Project

I would like to purchase a customized version of a design you have previously submitted - https://www.plomarket.com/design/7724163<br/><br/>I would like to incorporate the attached Images for my fitness company "TalvrenPro Athletics". My initial services is personal training and athletic performance. I would like a card that has one a shiny black side with the silver logo and the side with a white background utilizing the gold logo. On the white side, put "Sports Performance and Functional Strength Training" under the logo.
Industry/Entity Type
Fitness
Contact Information for Business Card
Marcus Tolley
Owner and Trainer
555.273.8492
marcus.tolley@talvrenproathletics.com
Look and feel
Each slider illustrates characteristics of the customer's brand and the style your logo design should communicate.

```html
<!DOCTYPE html>
<html lang="en">
<head>
<meta charset="UTF-8">
<title>TalvrenPro Athletics — Business Card</title>
<link rel="stylesheet" href="https://fonts.googleapis.com/css2?family=Roboto:wght@400;500&display=swap">
<style>
  :root {
    --backdrop: #1c1c1c;
    --card-black: #151515;
    --card-black-sheen: #2a2a2a;
    --card-white: #ffffff;
    --gold: #9c7f3f;
    --ink: #474747;
  }
  * { margin: 0; padding: 0; box-sizing: border-box; }
  html, body {
    width: 1200px;
    height: 900px;
    overflow: hidden;
    background: var(--backdrop);
    font-family: "Roboto", Arial, sans-serif;
  }
  .canvas {
    width: 1200px;
    height: 900px;
    display: flex;
    flex-direction: column;
    align-items: center;
    justify-content: center;
    gap: 20px;
  }
  .card {
    width: 700px;
    height: 400px;
    position: relative;
    overflow: hidden;
    box-shadow: 0 10px 30px rgba(0, 0, 0, 0.45);
  }
  .card--front {
    background: linear-gradient(120deg, var(--card-black) 0%, var(--card-black) 45%, var(--card-black-sheen) 100%);
    display: flex;
    align-items: center;
    justify-content: center;
  }
  .brand-mark {
    display: flex;
    align-items: center;
    gap: 14px;
  }
  .brand-mark__dot {
    width: 22px;
    height: 22px;
    border-radius: 50%;
    background: var(--gold);
  }
  .brand-mark__name {
    color: var(--gold);
    font-size: 30px;
    font-weight: 500;
    letter-spacing: 0.08em;
    text-transform: uppercase;
  }
  .card--back {
    background: var(--card-white);
    display: flex;
    flex-direction: column;
    align-items: center;
    justify-content: center;
    padding: 40px 48px;
  }
  .brand-mark--small { gap: 10px; }
  .brand-mark--small .brand-mark__dot { width: 16px; height: 16px; }
  .brand-mark--small .brand-mark__name { font-size: 20px; }
  .tagline {
    color: var(--ink);
    font-size: 14px;
    letter-spacing: 0.02em;
    margin-top: 8px;
  }
  .details {
    display: flex;
    align-items: center;
    gap: 24px;
    margin-top: 48px;
  }
  .identity { text-align: right; }
  .identity__name {
    color: var(--gold);
    font-size: 30px;
    font-weight: 400;
    letter-spacing: 0.01em;
    text-transform: uppercase;
    line-height: 1.05;
    white-space: nowrap;
  }
  .identity__title {
    color: var(--ink);
    font-size: 16px;
    margin-top: 4px;
  }
  .divider {
    width: 2px;
    height: 52px;
    background: var(--gold);
  }
  .contact { list-style: none; }
  .contact__item {
    display: flex;
    align-items: center;
    gap: 8px;
    color: var(--ink);
    font-size: 15px;
    line-height: 1.5;
    white-space: nowrap;
  }
  .contact__icon {
    width: 13px;
    height: 13px;
    flex: none;
  }
</style>
</head>
<body>
  <main class="canvas">
    <section class="card card--front" aria-label="Card front">
      <div class="brand-mark">
        <span class="brand-mark__dot"></span>
        <span class="brand-mark__name">TalvrenPro Athletics</span>
      </div>
    </section>

    <section class="card card--back" aria-label="Card back">
      <div class="brand-mark brand-mark--small">
        <span class="brand-mark__dot"></span>
        <span class="brand-mark__name">TalvrenPro Athletics</span>
      </div>
      <p class="tagline">Sports Performance and Functional Strength Training</p>
      <div class="details">
        <div class="identity">
          <h1 class="identity__name">Marcus Tolley</h1>
          <p class="identity__title">Owner and Trainer</p>
        </div>
        <span class="divider"></span>
        <ul class="contact">
          <li class="contact__item">
            <svg class="contact__icon" viewBox="0 0 24 24" aria-hidden="true">
              <path d="M6.6 10.8a15 15 0 0 0 6.6 6.6l2.2-2.2a1 1 0 0 1 1-.25 11.4 11.4 0 0 0 3.6.57 1 1 0 0 1 1 1V20a1 1 0 0 1-1 1A17 17 0 0 1 3 4a1 1 0 0 1 1-1h3.5a1 1 0 0 1 1 1c0 1.25.2 2.45.57 3.57a1 1 0 0 1-.25 1z" fill="#9c7f3f"/>
            </svg>
            <span>555.273.8492</span>
          </li>
          <li class="contact__item">
            <svg class="contact__icon" viewBox="0 0 24 24" aria-hidden="true">
              <rect x="2.5" y="5.5" width="19" height="13" fill="none" stroke="#9c7f3f" stroke-width="2"/>
              <path d="M3 6l9 7 9-7" fill="none" stroke="#9c7f3f" stroke-width="2"/>
            </svg>
            <span>marcus.tolley@talvrenproathletics.com</span>
          </li>
        </ul>
      </div>
    </section>
  </main>
</body>
</html>
```